PTA Business Card

Seeking design for a business card, standard size. It is going to be for myself in regards to PTA - details:

Hollis Fernway Elementary School
PTA President
Neil Brawley
555-208-3147
Brawl1984@mailnest.example

Requirement:
Facebook icon? "Hollis Fernway PTA Durn"
Twitter thing? I am new to twitter so not sure what to put, here is the link:
https://twitter.com/HFRoverbirdsPTA

I was thinking on the front would be a notebook paper background? Not a requirement but was thinking it would look cool?

Total freedom here, let your creativity spread because I don't have any suggestions for design, sorry. Colors of school district are black and yellow.

Backside I am not sure exactly what to put on it.

```html
<!DOCTYPE html>
<html lang="en">
<head>
<meta charset="UTF-8">
<title>Hollis Fernway PTA Business Card</title>
<link href="https://fonts.googleapis.com/css2?family=Arvo:wght@400;700&display=swap" rel="stylesheet">
<style>
  :root {
    --backdrop: #e9e4da;
    --paper: #fbf4c6;
    --rule: #b4c3de;
    --margin-red: #d8262c;
    --brand-red: #e3161b;
    --ink: #1b1b1b;
    --shadow: rgba(60, 40, 20, 0.25);
  }
  * { box-sizing: border-box; margin: 0; padding: 0; }
  html, body {
    width: 1200px; height: 900px; overflow: hidden;
    background: var(--backdrop);
    font-family: "Arvo", serif;
    color: var(--ink);
  }
  .stage {
    width: 1200px; height: 900px;
    display: flex; flex-direction: column;
    align-items: center; justify-content: center; gap: 40px;
  }
  .card {
    position: relative;
    width: 700px; height: 400px;
    background-color: var(--paper);
    background-image: repeating-linear-gradient(
      to bottom,
      transparent 0, transparent 23px,
      var(--rule) 23px, var(--rule) 24px);
    background-position: 0 12px;
    box-shadow: 0 8px 22px var(--shadow);
    overflow: hidden;
  }
  .margin-rule {
    position: absolute; top: 0; bottom: 0; width: 10px;
    border-left: 2px solid var(--margin-red);
    border-right: 2px solid var(--margin-red);
  }
  .card-front .margin-rule { right: 70px; }
  .card-back .margin-rule { left: 70px; }

  /* Front */
  .school-mark {
    position: absolute; top: 36px; left: 150px;
    display: flex; align-items: center; gap: 14px;
  }
  .school-mark-square {
    width: 56px; height: 56px; flex: none; background: var(--brand-red);
  }
  .school-mark-name {
    font-size: 26px; font-weight: 700; color: var(--brand-red);
    line-height: 1.15;
  }
  .district-mark {
    position: absolute; left: 40px; bottom: 36px;
    display: flex; align-items: center; gap: 10px;
  }
  .district-mark-square {
    width: 60px; height: 60px; flex: none; background: var(--ink);
  }
  .district-mark-name {
    font-size: 13px; line-height: 1.3; width: 110px;
  }
  .school-address {
    position: absolute; right: 110px; top: 168px;
    text-align: right;
  }
  .school-address-name {
    font-size: 36px; font-weight: 700; letter-spacing: 1px; line-height: 1.1;
  }
  .school-address-sub {
    font-size: 24px; line-height: 1.2;
  }
  .school-address-street {
    font-size: 14px; margin-top: 14px;
  }

  /* Back */
  .holder {
    position: absolute; left: 120px; top: 70px;
  }
  .holder-name {
    font-size: 38px; font-weight: 700; letter-spacing: 1.5px; line-height: 1.1;
  }
  .holder-role {
    font-size: 21px; margin-top: 4px;
  }
  .contact-list {
    position: absolute; right: 40px; top: 168px;
    list-style: none;
    display: flex; flex-direction: column; gap: 8px;
  }
  .contact-item {
    display: flex; align-items: center; gap: 12px;
    font-size: 21px; line-height: 1.2;
  }
  .contact-icon {
    width: 26px; height: 26px; flex: none;
    background: var(--brand-red); border-radius: 5px;
    display: flex; align-items: center; justify-content: center;
  }
  .contact-icon svg { width: 16px; height: 16px; }
</style>
</head>
<body>
<main class="stage">
  <section class="card card-front" aria-label="Card front">
    <div class="margin-rule"></div>
    <div class="school-mark">
      <span class="school-mark-square"></span>
      <span class="school-mark-name">Hollis Fernway<br>Elementary School</span>
    </div>
    <div class="district-mark">
      <span class="district-mark-square"></span>
      <span class="district-mark-name">Durnford Community School District</span>
    </div>
    <div class="school-address">
      <div class="school-address-name">HOLLIS FERNWAY</div>
      <div class="school-address-sub">Elementary School</div>
      <div class="school-address-street">384 Larkmoor Rd., Durnford, OR 97845</div>
    </div>
  </section>

  <section class="card card-back" aria-label="Card back">
    <div class="margin-rule"></div>
    <div class="holder">
      <div class="holder-name">NEIL BRAWLEY</div>
      <div class="holder-role">PTA President</div>
    </div>
    <ul class="contact-list">
      <li class="contact-item">
        <span class="contact-icon">
          <svg viewBox="0 0 16 16"><path d="M3 1.5l3 .5 1 3-1.7 1.3a8 8 0 0 0 4.4 4.4L11 9l3 1 .5 3-1.8 1.6C7.5 14.6 1.4 8.5 1.4 3.3z" fill="#fff"/></svg>
        </span>
        <span>555-208-3147</span>
      </li>
      <li class="contact-item">
        <span class="contact-icon">
          <svg viewBox="0 0 16 16"><rect x="1.5" y="3.5" width="13" height="9" rx="1" fill="none" stroke="#fff" stroke-width="1.6"/><path d="M2 4.5l6 4.5 6-4.5" fill="none" stroke="#fff" stroke-width="1.6"/></svg>
        </span>
        <span>Brawl1984@mailnest.example</span>
      </li>
      <li class="contact-item">
        <span class="contact-icon"></span>
        <span>Hollis Fernway PTA Durn</span>
      </li>
      <li class="contact-item">
        <span class="contact-icon"></span>
        <span>HFRoverbirdsPTA</span>
      </li>
    </ul>
  </section>
</main>
</body>
</html>
```